Dravel

We are openıng one huntıng showroom in Riyadh? Saudi Arabia. Company name is "DRAVEL".
Our logo designed and we need Business Card Design now.
I attached DRAVEL logo below.
Front side will English and back side will be Arabic

```html
<!DOCTYPE html>
<html lang="en">
<head>
<meta charset="utf-8">
<title>Dravel Business Card</title>
<link href="https://fonts.googleapis.com/css2?family=Open+Sans:wght@400;600;700;800&family=Noto+Kufi+Arabic:wght@400;600&display=swap" rel="stylesheet">
<style>
  :root {
    --green: #086b3c;
    --green-dark: #065a32;
    --olive: #6a9a3a;
    --white: #ffffff;
    --paper: #f6f6f6;
    --ink: #222222;
    --canvas: #e4e4e4;
  }
  * { margin: 0; padding: 0; box-sizing: border-box; }
  html, body { width: 1200px; height: 1021px; overflow: hidden; }
  body {
    background: var(--canvas);
    font-family: "Open Sans", sans-serif;
    position: relative;
  }
  .card {
    position: absolute;
    left: 200px;
    width: 800px;
    height: 457px;
    overflow: hidden;
    box-shadow: 0 4px 14px rgba(0,0,0,0.18);
  }
  .card--back { top: 30px; background: var(--green); color: var(--white); }
  .card--front { top: 534px; background: linear-gradient(135deg, #ffffff 0%, #ededed 100%); color: var(--ink); }

  /* side tabs */
  .tab { position: absolute; width: 30px; }
  .card--front .tab { left: 0; top: 120px; height: 215px; background: var(--green); border-radius: 0 22px 22px 0; }
  .card--back .tab { right: 0; top: 120px; height: 215px; background: var(--olive); border-radius: 22px 0 0 22px; }

  /* wordmark */
  .wordmark {
    position: absolute;
    font-family: "Open Sans", sans-serif;
    font-weight: 800;
    font-size: 82px;
    letter-spacing: 2px;
    line-height: 1;
    display: flex;
    align-items: center;
    gap: 14px;
  }
  .wordmark .mark-dot { width: 18px; height: 18px; }
  .card--front .wordmark { right: 60px; top: 190px; color: var(--green); }
  .card--front .wordmark .mark-dot { background: var(--green); }
  .card--back .wordmark { left: 70px; top: 160px; color: var(--white); }
  .card--back .wordmark .mark-dot { background: var(--white); }

  /* front details */
  .details { position: absolute; left: 70px; top: 80px; }
  .details .name { font-size: 26px; font-weight: 700; color: var(--green); line-height: 1.1; }
  .details .role { font-size: 18px; color: #333; margin-top: 2px; }
  .rule { width: 26px; height: 3px; background: var(--olive); margin: 16px 0 14px; }
  .address { font-size: 18px; line-height: 1.35; color: var(--ink); }
  .contacts { list-style: none; margin-top: 6px; font-size: 18px; line-height: 1.45; }
  .contacts li { display: flex; align-items: center; gap: 10px; }
  .contacts svg { width: 16px; height: 16px; flex: none; }
  .card--front .contacts svg { fill: none; stroke: var(--olive); stroke-width: 2; }

  /* back details (Arabic) */
  .details-ar {
    position: absolute;
    right: 70px;
    top: 95px;
    text-align: right;
    font-family: "Noto Kufi Arabic", sans-serif;
  }
  .details-ar .name { font-size: 24px; font-weight: 600; line-height: 1.3; }
  .details-ar .role { font-size: 16px; }
  .details-ar .rule { margin-left: auto; background: var(--white); }
  .details-ar .address { font-size: 16px; color: var(--white); line-height: 1.5; }
  .details-ar .contacts { font-family: "Open Sans", sans-serif; }
  .details-ar .contacts li { justify-content: flex-end; direction: ltr; }
  .card--back .contacts svg { fill: none; stroke: var(--white); stroke-width: 2; }
</style>
</head>
<body>

<section class="card card--back" dir="rtl" lang="ar">
  <div class="wordmark" dir="ltr"><span class="mark-dot"></span>DRAVEL</div>
  <div class="details-ar">
    <p class="name">عمر حداد</p>
    <p class="role">المؤسس</p>
    <div class="rule"></div>
    <p class="address">الطابق ١٤، برج النور<br>شارع بالم جروف، الخبر ٣١٩٥٠</p>
    <ul class="contacts">
      <li>+966 50 214 8630 <svg viewBox="0 0 16 16"><path d="M4 1.5l2.5 3-1.5 2a8 8 0 0 0 4.5 4.5l2-1.5 3 2.5-1.5 2.5C7 14 2 9 1.5 3z"/></svg></li>
      <li>omar@dravel.com <svg viewBox="0 0 16 16"><rect x="1.5" y="3.5" width="13" height="9"/><path d="M1.5 3.5l6.5 5 6.5-5"/></svg></li>
      <li>www.dravel.com <svg viewBox="0 0 16 16"><circle cx="8" cy="8" r="6.5"/><path d="M1.5 8h13M8 1.5c-3 3.5-3 9.5 0 13M8 1.5c3 3.5 3 9.5 0 13"/></svg></li>
    </ul>
  </div>
  <div class="tab"></div>
</section>

<section class="card card--front">
  <div class="tab"></div>
  <div class="details">
    <p class="name">Omar Haddad</p>
    <p class="role">Founder</p>
    <div class="rule"></div>
    <p class="address">Level 14, Al Noor Tower<br>Palm Grove Street, Al Khobar 31950</p>
    <ul class="contacts">
      <li><svg viewBox="0 0 16 16"><path d="M4 1.5l2.5 3-1.5 2a8 8 0 0 0 4.5 4.5l2-1.5 3 2.5-1.5 2.5C7 14 2 9 1.5 3z"/></svg>+966 50 214 8630</li>
      <li><svg viewBox="0 0 16 16"><rect x="1.5" y="3.5" width="13" height="9"/><path d="M1.5 3.5l6.5 5 6.5-5"/></svg>omar@dravel.com</li>
      <li><svg viewBox="0 0 16 16"><circle cx="8" cy="8" r="6.5"/><path d="M1.5 8h13M8 1.5c-3 3.5-3 9.5 0 13M8 1.5c3 3.5 3 9.5 0 13"/></svg>www.dravel.com</li>
    </ul>
  </div>
  <div class="wordmark"><span class="mark-dot"></span>DRAVEL</div>
</section>

</body>
</html>
```